KORVa: AI driven decarbonization application

We are seeking an engaging, user-friendly, and visually appealing user interface for our B2B SaaS platform, Brelmont KORVa. This solution helps large organizations achieve net-zero emissions using AI-driven forecasting, AI models, a emission mitigation library, and a scenario simulator..

A big challenge is to allow the user to work efficiently with multidimensional data.

Requirements:

* Design a modern, professional, and visually striking user interface, catering to a diverse audience within large corporations, including executives, strategists, and environmental specialists.

* Construct an intuitive navigation system, allowing users to seamlessly access functionalities for informed decision-making and tracking progress towards net-zero emissions.

* The application is expected to be used on desktops first

* Incorporate our brand's colors, and visual elements into the design to maintain consistency throughout the application.

* Provide design assets and documentation, such as style guides, design specifications, and necessary assets (e.g., icons, illustrations) for our development team to implement the design. We use Figma and would appreciate delivery as figma files.

Please note that we also need more pages over time. The most important is to get the work bench page right. We will also need:
* a landing page where the users can select previous scenarios and see some high level data.
* A page with information on historical data per asset
* An analytics page
* User and system administration pages.
These pages are out of scope for this project, but they should be available in the navigation solution.

Please submit your initial design concepts, accompanied by a brief explanation of your approach and the rationale behind your design choices. We will offer feedback and collaborate with the chosen designer to refine the design, ensuring it meets our requirements and vision.

We are really hoping to see some elegant user interfaces. The functionality describe in the attachment is important, but the layout is not. Feel free to invent.

Attached files:

Target Market(s)

Energy intensive industries

Requirements
Must have
• Easy to navigate through the different data dimensions: Time, assets, mitigation measures, and advanced details under mitigation measures. The design in the attached files are just our working drafts. Creative alternatives are very welcome.
Nice to have
• Elegant layouts that differ from our working drafts.

```html
<!DOCTYPE html>
<html lang="en">
<head>
<meta charset="utf-8">
<title>Brelmont KORVa – Style Guide</title>
<link href="https://fonts.googleapis.com/css2?family=Saira:wght@400;600;700&family=Mulish:wght@400;600;700&display=swap" rel="stylesheet">
<style>
  :root{
    --blue:#1E5F96;
    --blue-light:#2577bd;
    --teal:#5D9797;
    --panel:#f4f4f4;
    --white:#ffffff;
    --row:#2c6ba4;
    --ink-soft:#6f8fa8;
    --saira:"Saira", sans-serif;
    --mulish:"Mulish", sans-serif;
  }
  *{box-sizing:border-box;margin:0;padding:0}
  html,body{width:1200px;height:4162px;overflow:hidden;background:var(--white)}
  body{position:relative;font-family:var(--mulish);color:var(--blue)}
  .abs{position:absolute}

  /* Header */
  .brand{left:0;width:1200px;top:132px;text-align:center;font-family:var(--saira);font-weight:600;font-size:64px;letter-spacing:6px;color:var(--blue);line-height:1}
  .hero-title{left:0;width:1200px;top:316px;text-align:center;font-family:var(--saira);font-weight:700;font-size:70px;line-height:84px;color:var(--blue)}
  .hero-sub{left:180px;top:630px;font-size:25px;line-height:38px;color:var(--teal)}

  /* Colour panel */
  .color-panel{left:58px;top:784px;width:1072px;height:640px;background:var(--panel)}
  .color-title{left:91px;top:92px;font-family:var(--saira);font-weight:700;font-size:66px;line-height:82px;color:var(--blue)}
  .swatch{width:176px;height:176px;border-radius:50%;top:347px}
  .swatch.blue{left:91px;background:var(--blue)}
  .swatch.teal{left:545px;background:var(--teal)}
  .spec{top:362px;display:grid;grid-template-columns:70px auto;row-gap:15px;font-size:17px;line-height:23px}
  .spec dt{font-weight:700}
  .spec.blue{left:283px;color:var(--blue)}
  .spec.blue dd{color:var(--blue)}
  .spec.teal{left:737px;color:var(--teal)}

  /* Typography cards */
  .card{border-radius:10px;color:var(--white)}
  .card.blue{background:var(--blue)}
  .card.teal{background:var(--teal)}
  .face-label{font-size:24px;letter-spacing:1px;line-height:1}
  .face-name{font-size:52px;font-weight:700;line-height:1}
  .face-sample{font-size:130px;line-height:1}
  .lorem{font-size:11px;line-height:17px;width:420px}
  .weight-name{font-size:46px;line-height:1}
  .w400{font-weight:400}.w600{font-weight:600}.w700{font-weight:700}
  .saira{font-family:var(--saira)}
  .mulish{font-family:var(--mulish)}

  /* App screen */
  .app{left:58px;top:2986px;width:1072px;height:960px;border-radius:10px;overflow:hidden;background:linear-gradient(180deg,#1d5c93 0%,#2477bd 100%)}
  .topbar{left:0;top:0;width:1072px;height:48px;background:var(--white)}
  .app-brand{left:51px;top:12px;font-family:var(--saira);font-weight:600;font-size:20px;letter-spacing:2px;color:var(--blue);line-height:1}
  .nav{left:406px;top:20px;display:flex;align-items:flex-end;height:28px;font-size:12px;color:var(--ink-soft)}
  .nav span{padding:0 12px 5px}
  .nav .active{background:var(--teal);color:var(--white);font-weight:700;border-radius:6px 6px 0 0;padding:7px 12px 5px;font-family:var(--saira)}
  .user{left:913px;top:14px;text-align:right;font-family:var(--saira);font-weight:700;font-size:11px;line-height:1.1;color:var(--blue)}
  .user small{display:block;font-weight:400;font-size:6px;color:var(--ink-soft)}
  .avatar{left:992px;top:10px;width:26px;height:26px;border-radius:50%;border:2px solid #cfdbe6}

  .side-title{left:52px;top:94px;font-family:var(--saira);font-weight:700;font-size:22px;line-height:1;color:var(--white)}
  .menu{left:52px;width:231px;list-style:none}
  .menu-head{height:32px;background:var(--white);border-radius:3px;display:flex;align-items:center;justify-content:space-between;padding:0 10px;font-family:var(--saira);font-weight:700;font-size:14px;color:var(--blue);margin-bottom:5px}
  .chev{width:7px;height:7px;border-right:1.5px solid var(--blue);border-bottom:1.5px solid var(--blue)}
  .chev.down{transform:rotate(45deg) translateY(-3px)}
  .chev.left{transform:rotate(135deg)}
  .menu-item{height:32px;margin-bottom:5px;background:var(--row);display:flex;align-items:center;justify-content:space-between;padding:0 10px;font-size:11.5px;color:var(--white)}
  .check{width:11px;height:11px;background:var(--white);border-radius:2px;position:relative}
  .check::after{content:"";position:absolute;left:3px;top:1px;width:3px;height:6px;border-right:2px solid var(--blue);border-bottom:2px solid var(--blue);transform:rotate(45deg)}

  .chart-card{left:297px;top:100px;width:723px;height:645px;background:var(--white);border-radius:14px;overflow:hidden}
  .map-fill{left:90px;top:140px;width:600px;height:300px;background:radial-gradient(ellipse at center,#eef3f8 0%,rgba(238,243,248,0) 70%)}
  .chart{left:0;top:0;width:723px;height:645px}
  .goal{left:376px;top:478px;font-family:var(--saira);font-weight:600;font-size:19px;color:var(--teal)}
  .y-title{left:-80px;top:300px;width:280px;transform:rotate(-90deg);text-align:center;font-size:12px;color:var(--blue)}

  .thanks{left:0;width:1200px;top:3980px;text-align:center;font-family:var(--saira);font-weight:700;font-size:100px;letter-spacing:44px;line-height:1;color:var(--blue);padding-left:20px}
</style>
</head>
<body>

<header>
  <div class="abs brand">BRELMONT</div>
  <h1 class="abs hero-title">Find The Most<br>Efficient Path To Net Zero</h1>
  <p class="abs hero-sub">AI driven scenario predictions<br>for GHG reductions</p>
</header>

<section class="abs color-panel">
  <h2 class="abs color-title">Color<br>Alternative</h2>
  <div class="abs swatch blue"></div>
  <dl class="abs spec blue">
    <dt>HEX</dt><dd>#1E5F96</dd>
    <dt>HSB</dt><dd>207, 80%, 59%</dd>
    <dt>RGB</dt><dd>30, 95, 150</dd>
    <dt>CMYK</dt><dd>92%, 65%, 17%, 2%</dd>
  </dl>
  <div class="abs swatch teal"></div>
  <dl class="abs spec teal">
    <dt>HEX</dt><dd>#5D9797</dd>
    <dt>HSB</dt><dd>180, 38%, 59%</dd>
    <dt>RGB</dt><dd>93, 151, 151</dd>
    <dt>CMYK</dt><dd>66%, 26%, 40%, 2%</dd>
  </dl>
</section>

<!-- Saira -->
<section class="abs card blue saira" style="left:421px;top:1526px;width:707px;height:642px">
  <div class="abs weight-name w600" style="left:179px;top:64px">Regular</div>
  <p class="abs lorem w400" style="left:180px;top:130px">Lorem Ipsum is simply dummy text of the printing and typesetting industry. Lorem Ipsum has been the industry's standard dummy text ever since the 1500s, when an unknown printer took a galley of type and scrambled it to make a type specimen book.</p>
  <div class="abs weight-name w600" style="left:179px;top:262px">Semibold</div>
  <p class="abs lorem w600" style="left:180px;top:328px">Lorem Ipsum is simply dummy text of the printing and typesetting industry. Lorem Ipsum has been the industry's standard dummy text ever since the 1500s, when an unknown printer took a galley of type and scrambled it to make a type specimen book.</p>
  <div class="abs weight-name w700" style="left:179px;top:460px">Bold</div>
  <p class="abs lorem w700" style="left:180px;top:526px">Lorem Ipsum is simply dummy text of the printing and typesetting industry. Lorem Ipsum has been the industry's standard dummy text ever since the 1500s, when an unknown printer took a galley of type and scrambled it to make a type specimen book.</p>
</section>
<section class="abs card teal" style="left:58px;top:1632px;width:483px;height:429px">
  <div class="abs face-label mulish" style="left:33px;top:52px">TYPOGRAPHY</div>
  <div class="abs face-name saira" style="left:33px;top:106px">SAIRA</div>
  <div class="abs face-sample saira w700" style="left:30px;top:180px">Aa</div>
  <p class="abs lorem saira" style="left:35px;top:310px">Lorem Ipsum is simply dummy text of the printing and typesetting industry. Lorem Ipsum has been the industry's standard dummy text ever since the 1500s, when an unknown printer took a galley of type and scrambled it to make a type specimen book.</p>
</section>

<!-- Mulish -->
<section class="abs card blue mulish" style="left:58px;top:2234px;width:707px;height:640px">
  <div class="abs weight-name w400" style="left:91px;top:64px">Regular</div>
  <p class="abs lorem w400" style="left:91px;top:130px">Lorem Ipsum is simply dummy text of the printing and typesetting industry. Lorem Ipsum has been the industry's standard dummy text ever since the 1500s, when an unknown printer took a galley of type and scrambled it to make a type specimen book.</p>
  <div class="abs weight-name w600" style="left:88px;top:262px">Semibold</div>
  <p class="abs lorem w600" style="left:91px;top:328px">Lorem Ipsum is simply dummy text of the printing and typesetting industry. Lorem Ipsum has been the industry's standard dummy text ever since the 1500s, when an unknown printer took a galley of type and scrambled it to make a type specimen book.</p>
  <div class="abs weight-name w700" style="left:88px;top:460px">Bold</div>
  <p class="abs lorem w700" style="left:91px;top:526px">Lorem Ipsum is simply dummy text of the printing and typesetting industry. Lorem Ipsum has been the industry's standard dummy text ever since the 1500s, when an unknown printer took a galley of type and scrambled it to make a type specimen book.</p>
</section>
<section class="abs card teal mulish" style="left:645px;top:2339px;width:483px;height:429px">
  <div class="abs face-label" style="left:33px;top:52px">TYPOGRAPHY</div>
  <div class="abs face-name w400" style="left:33px;top:106px">MULISH</div>
  <div class="abs face-sample w400" style="left:30px;top:180px">Aa</div>
  <p class="abs lorem" style="left:35px;top:310px">Lorem Ipsum is simply dummy text of the printing and typesetting industry. Lorem Ipsum has been the industry's standard dummy text ever since the 1500s, when an unknown printer took a galley of type and scrambled it to make a type specimen book.</p>
</section>

<!-- Workbench screen -->
<section class="abs app">
  <div class="abs topbar">
    <div class="abs app-brand">BRELMONT</div>
    <nav class="abs nav"><span>Home</span><span>Assets</span><span class="active">SCENARIO SIMULATION</span><span>Map</span></nav>
    <div class="abs user">HELENA<small>My Company</small></div>
    <div class="abs avatar"></div>
  </div>

  <h3 class="abs side-title">Scenario Tuning</h3>
  <ul class="abs menu" style="top:136px">
    <li class="menu-head">Switch Energy Carrier<span class="chev down"></span></li>
    <li class="menu-item">Switch Energy Carrier<span class="check"></span></li>
    <li class="menu-item">Biodiesel<span class="check"></span></li>
    <li class="menu-item">Ethanol<span class="check"></span></li>
    <li class="menu-item">Hydrogen<span class="check"></span></li>
    <li class="menu-item">Methanol<span class="check"></span></li>
    <li class="menu-item">Power from offshore wind<span class="check"></span></li>
    <li class="menu-item">Power form shore<span class="check"></span></li>
  </ul>
  <ul class="abs menu" style="top:439px">
    <li class="menu-head">Energy efficiency measures<span class="chev down"></span></li>
    <li class="menu-item">Venting to flare<span class="check"></span></li>
    <li class="menu-item">Venting to production<span class="check"></span></li>
    <li class="menu-item">Fugitive emission measure<span class="check"></span></li>
    <li class="menu-item">Compressor replacement<span class="check"></span></li>
    <li class="menu-item">Reduced water injection<span class="check"></span></li>
    <li class="menu-item">Reduced gas injection<span class="check"></span></li>
    <li class="menu-item">Drilling improvements<span class="check"></span></li>
  </ul>
  <ul class="abs menu" style="top:769px">
    <li class="menu-head">Logistics<span class="chev left"></span></li>
    <li class="menu-head">End of pipe measures<span class="chev left"></span></li>
    <li class="menu-head">Carbon Offsets<span class="chev left"></span></li>
    <li class="menu-head">Company Structure<span class="chev left"></span></li>
  </ul>

  <div class="abs chart-card">
    <div class="abs map-fill" role="img" aria-label="Faint world map behind the emissions chart"></div>
    <svg class="abs chart" viewBox="222 1929 452 403" aria-label="Relative emissions scenarios 2010 to 2045">
      <g font-family="Mulish, sans-serif" font-size="6" fill="#1E5F96" text-anchor="end">
        <text x="262" y="1952">20</text>
        <text x="262" y="2030">15</text>
        <text x="262" y="2117">10</text>
        <text x="262" y="2225">5</text>
        <text x="262" y="2298">0</text>
      </g>
      <g font-family="Mulish, sans-serif" font-size="6" fill="#1E5F96" text-anchor="middle">
        <text x="272" y="2306">2010</text>
        <text x="371" y="2306">2020</text>
        <text x="470" y="2306">2030</text>
        <text x="570" y="2306">2040</text>
      </g>
      <line x1="265" y1="1946" x2="265" y2="2296" stroke="#c9d6e2" stroke-width="0.6"/>
      <line x1="265" y1="2296" x2="655" y2="2296" stroke="#c9d6e2" stroke-width="0.6"/>
      <g fill="none" stroke-width="1.4" stroke-linecap="round">
        <path stroke="#c6c65a" d="M470 2196 C495 2180 520 2172 545 2180 S610 2202 652 2202"/>
        <path stroke="#7fd16a" d="M264 2170 C278 2205 292 2225 305 2210 S335 2010 350 2008 S378 2205 395 2210 S420 2135 430 2140 S450 2220 460 2215 S490 2175 520 2175"/>
        <path stroke="#6ec8f0" d="M264 2120 C280 2108 292 2110 305 2125 S335 2180 350 2170 S385 2080 397 2085 S408 2165 418 2162 S450 2085 462 2092 S474 2165 487 2160 S510 2150 520 2150"/>
        <path stroke="#8e3f7e" d="M264 2155 C275 2095 290 2038 302 2040 S330 2170 348 2200 S400 2130 427 2128 S490 2190 520 2190 S610 2125 652 2118"/>
        <path stroke="#a889db" d="M430 2132 C470 2150 495 2185 520 2186 S605 2130 652 2118"/>
        <path stroke="#b24fd8" d="M430 2128 C465 2150 490 2184 520 2184 S600 2095 652 2078"/>
      </g>
    </svg>
    <div class="abs y-title">Relative Emissions, Kg CO2e / produced unit</div>
    <div class="abs goal">Company Goal</div>
  </div>
</section>

<div class="abs thanks">THNAK YOU</div>

</body>
</html>
```